female stress management consultant, doctor, Health & Well-being coach needs a wordpress theme

I am a Stress management consultant, General Practitioner and Health and Well-Being coach who is targeting mainly surgeries/hospitals and corporate business.
I have my own URL drhelgabrunsvik.com and the hosting.
I need a WordPress Website that is easy to maintain and edit to regularly change the content (copy/pictures/action buttons/banners).
I want my website to look professional and elegant for corporate businesses and managers to feel they can trust me and my expertise. At the same time, the website should have a warm and welcoming feel to it. It should feel uplifting and very positive.
I am open to colour suggestions, but please incorporate the following two colours: #F18877 and #D2BB7A. For fonts I prefer grey over black (like #777777).
The website needs to create an impression of "know like and trust".
The website should have a sign-up button for a newsletter, multiple contact buttons over the home page - to write an email to me, contact details top and bottom and the possibility to have a video on the home page top instead of a picture (Best would be that I can change from picture to video to picture in the future without needing a designer). A video that can run in the background with text laid over. A bit like on this website from Tessa Lindqvor: https://www.tessalindqvor.com.
I need 5 pages: Home, About, Services, Contact, free resources. I do NOT need an e-commerce or booking facility as I will neither sell nor let people book through my website. I don't need a blog either.
All the pages need to have a link to my other website (brightpathdaily.co.uk) and it needs to state that the linked website (brightpathdaily) is my website with a blog and for private customers.
Please use the photos I attached if possible. Me with the dogs for the "about" section.

Websites I like: https://www.rosalbkq.com, tessalindqvor.com, https://pennyholtzbrook.com (this site is too dark for my liking, but the layout has a simple navigation layout, the important buttons are right up at the side (LinkedIn/social media/CTA), is minimalistic - hence easy to find the important bits).

surgeries/doctor offices, hospitals, corporate business

Health and well-being

5+ page

Sans Serif

• see project description
• see project description

```html
<!DOCTYPE html>
<html lang="en">
<head>
<meta charset="utf-8">
<title>Dr Helga Brunsvik – Health &amp; Well-Being</title>
<link rel="stylesheet" href="https://fonts.googleapis.com/css2?family=Poppins:wght@300;400;500;600&display=swap">
<style>
:root{
  --coral:#F18877;
  --coral-dark:#e4735f;
  --gold:#D2BB7A;
  --cream:#FDF5E2;
  --grey:#777777;
  --grey-dark:#444444;
  --white:#ffffff;
  --line:#e8e8e8;
}
*{box-sizing:border-box;margin:0;padding:0}
html,body{width:1200px;height:5300px;overflow:hidden}
body{font-family:'Poppins',sans-serif;color:var(--grey);background:var(--white);position:relative}
section,header,footer{position:absolute;left:0;width:1200px}
.abs{position:absolute}

/* header */
.site-header{top:0;height:156px;background:var(--white)}
.brand{left:82px;top:52px;display:flex;align-items:center;gap:12px}
.brand-dot{width:34px;height:34px;border-radius:50%;background:var(--coral)}
.brand-name{font-size:19px;font-weight:400;color:var(--coral)}
.pill{top:35px;height:37px;border-radius:19px;background:var(--coral);color:var(--white);font-size:13px;display:flex;align-items:center;gap:10px;padding:0 14px 0 5px}
.pill-icon{width:28px;height:28px;border-radius:50%;background:var(--white);display:flex;align-items:center;justify-content:center}
.pill-phone{left:673px;width:165px}
.pill-mail{left:860px;width:253px}
.main-nav{top:98px;right:87px;display:flex;gap:26px;font-size:15px}
.main-nav a{color:var(--grey);text-decoration:none}
.main-nav a.current{color:var(--coral)}

/* hero */
.hero{top:156px;height:735px;background:radial-gradient(ellipse at 40% 30%,#4b5640 0%,#2d3428 55%,#1d231b 100%)}
.hero-media{position:absolute;inset:0}
.hero-title{top:320px;width:100%;text-align:center;color:var(--white);font-size:37px;font-weight:300;line-height:52px}
.watch{top:476px;left:0;width:100%;display:flex;justify-content:center;align-items:center;gap:12px;color:var(--white);font-size:19px;font-weight:500}
.chevron{top:668px;left:584px}

/* health talk bar */
.talk-bar{top:891px;height:179px;background:var(--white)}
.talk-title{left:111px;top:56px;font-size:41px;font-weight:300;color:var(--coral)}
.join{left:514px;top:58px;width:351px;height:52px;border-bottom:3px solid var(--coral);display:flex;align-items:center;gap:12px;font-size:30px;font-weight:300;color:var(--grey-dark);padding-left:6px}
.social-row{left:967px;top:71px;display:flex;gap:12px}
.social-row span{width:30px;height:30px;border-radius:50%;background:var(--coral)}

/* about */
.about{top:1070px;height:642px;background:var(--cream)}
.about-band{left:900px;top:0;width:300px;height:642px;background:var(--coral)}
.about-ring{left:543px;top:16px;width:618px;height:618px;border-radius:50%;background:var(--white)}
.about-inner{left:567px;top:40px;width:570px;height:570px;border-radius:50%;background:var(--coral)}
.about-photo{left:591px;top:64px;width:522px;height:522px;border-radius:50%;background:radial-gradient(circle at 45% 40%,#c9b6a4 0%,#8c9470 45%,#5b6e45 100%)}
.about-title{left:86px;top:104px;font-size:37px;font-weight:300;color:var(--coral)}
.about-lead{left:86px;top:170px;width:420px;font-size:25px;line-height:34px;font-weight:500;color:var(--grey-dark)}
.about-text{left:86px;top:330px;width:392px;font-size:14.5px;line-height:31px;color:var(--grey);text-align:justify}
.btn-coral{background:var(--coral);color:var(--white);border-radius:8px;font-size:14px;font-weight:500;display:flex;align-items:center;justify-content:center}
.about-btn{left:86px;top:550px;width:216px;height:62px}

/* services */
.services{top:1712px;height:1360px;background:var(--white)}
.section-title{width:100%;text-align:center;font-size:50px;font-weight:300;color:var(--coral)}
.services .section-title{top:98px}
.service{left:82px;width:1031px;height:311px;background:var(--white);box-shadow:0 2px 12px rgba(0,0,0,.12)}
.service-photo{position:absolute;top:9px;width:498px;height:293px}
.service-body{position:absolute;top:50px;width:420px}
.service-body h3{font-size:26px;font-weight:300;color:var(--coral);margin-bottom:18px}
.service-body p{font-size:14px;line-height:26px;color:var(--grey);text-align:justify}
.read-more{margin-top:22px;font-size:11.5px;color:var(--coral);display:flex;align-items:center;gap:6px}
.s1{top:247px}.s2{top:593px}.s3{top:937px}
.photo-left{left:9px}.photo-right{right:9px}
.body-right{left:560px}.body-left{left:60px;text-align:right}
.body-left h3{text-align:right}
.body-left .read-more{justify-content:flex-end}

/* call to action */
.cta{top:3072px;height:439px;background:var(--coral)}
.cta-title{top:118px;width:100%;text-align:center;color:var(--white);font-size:40px;font-weight:300;line-height:52px}
.cta-btn{top:252px;height:96px;border-radius:6px;display:flex;align-items:center;justify-content:center;font-size:40px;font-weight:500}
.cta-site{left:181px;width:488px;background:var(--white);color:var(--coral)}
.cta-contact{left:685px;width:336px;border:2px solid var(--white);color:var(--white)}

/* testimonials */
.testimonials{top:3511px;height:691px;background:var(--white)}
.testimonials .section-title{top:110px;font-size:42px}
.quote-card{top:255px;width:328px;height:288px;border-radius:14px;background:var(--white);box-shadow:0 2px 14px rgba(0,0,0,.1);padding:80px 26px 0}
.quote-mark{position:absolute;left:26px;top:-34px;width:74px;height:74px;border-radius:50%;background:var(--coral);color:var(--white);font-size:52px;font-weight:600;display:flex;align-items:center;justify-content:center;line-height:1;padding-top:18px}
.stars{display:flex;gap:3px;margin-bottom:12px}
.quote-card p{font-size:14.5px;line-height:26px;color:var(--grey-dark);text-align:justify;height:92px;border-bottom:1px solid var(--line);margin-bottom:22px}
.author{display:flex;align-items:center;gap:14px}
.avatar{width:38px;height:38px;border-radius:50%;background:linear-gradient(135deg,#b9a597,#6b6560)}
.author b{display:block;font-size:14px;font-weight:600;color:var(--grey-dark)}
.author span{font-size:13px;color:var(--grey)}
.t1{left:86px}.t2{left:436px}.t3{left:784px}
.dots{top:596px;left:564px;display:flex;gap:6px}
.dots span{width:14px;height:14px;border-radius:50%;background:#f7d3cc}
.dots span:first-child{background:var(--coral)}

/* newsletter */
.newsletter{top:4202px;height:449px;background:var(--gold)}
.newsletter-title{top:100px;width:100%;text-align:center;color:var(--white);font-size:41px;font-weight:300;line-height:52px}
.newsletter-sub{top:233px;width:100%;text-align:center;color:var(--white);font-size:19px;font-weight:500}
.newsletter-form{left:276px;top:291px;width:648px;height:72px;border-radius:36px;background:var(--white)}
.newsletter-form .field{position:absolute;left:40px;top:25px;font-size:14px;color:var(--grey)}
.subscribe{position:absolute;right:0;top:0;width:195px;height:72px;border-radius:36px;background:var(--coral);color:var(--white);font-size:21px;display:flex;align-items:center;justify-content:center}

/* footer */
.site-footer{top:4651px;height:649px;background:var(--coral);color:var(--white)}
.footer-brand{top:130px;width:100%;display:flex;justify-content:center;align-items:center;gap:12px;font-size:20px;font-weight:400}
.footer-brand i{width:30px;height:30px;border-radius:50%;background:var(--white)}
.footer-heading{top:252px;font-size:23px;font-weight:400;text-transform:uppercase}
.fh1{left:82px}.fh2{left:611px}.fh3{left:955px}
.input{background:var(--white);color:var(--grey);font-size:11px;padding:14px 16px;height:43px}
.f-first{left:82px;top:317px;width:210px}
.f-last{left:302px;top:317px;width:206px}
.f-email{left:82px;top:371px;width:210px}
.f-phone{left:302px;top:371px;width:206px}
.f-message{left:82px;top:424px;width:426px;height:66px}
.f-submit{left:82px;top:502px;width:142px;height:46px;background:var(--gold);color:var(--white);font-size:14px;display:flex;align-items:center;justify-content:center}
.contact-item{left:611px;display:flex;gap:16px;align-items:flex-start}
.contact-icon{width:54px;height:54px;border-radius:50%;border:2px solid var(--white);display:flex;align-items:center;justify-content:center;flex:none}
.contact-item b{display:block;font-size:15px;font-weight:500;margin-top:4px}
.contact-item span{font-size:14px;line-height:18px;display:block}
.ci1{top:318px}.ci2{top:404px}.ci3{top:491px}
.quick-links{left:955px;top:323px;list-style:none;font-size:14.5px}
.quick-links li{height:41px}
.quick-links li::before{content:"›› ";font-size:12px;margin-right:6px}
.footer-social{left:960px;top:500px;display:flex;gap:8px}
.footer-social span{width:32px;height:32px;border-radius:50%;background:var(--white)}
.footer-rule{left:82px;top:588px;width:1031px;height:1px;background:rgba(255,255,255,.6)}
.copyright{left:82px;top:605px;font-size:13px}
.legal{right:87px;top:605px;font-size:13px}
</style>
</head>
<body>

<header class="site-header">
  <div class="abs brand"><span class="brand-dot"></span><span class="brand-name">Dr Helga Brunsvik</span></div>
  <div class="abs pill pill-phone"><span class="pill-icon"><svg width="14" height="14" viewBox="0 0 24 24"><path d="M6.6 10.8a15 15 0 006.6 6.6l2.2-2.2c.3-.3.7-.4 1-.2 1.1.4 2.3.6 3.6.6.6 0 1 .4 1 1V20c0 .6-.4 1-1 1A17 17 0 013 4c0-.6.4-1 1-1h3.5c.6 0 1 .4 1 1 0 1.2.2 2.4.6 3.6.1.3 0 .7-.2 1z" fill="#F18877"/></svg></span>904-555-0173</div>
  <div class="abs pill pill-mail"><span class="pill-icon"><svg width="14" height="12" viewBox="0 0 24 18"><rect x="1" y="1" width="22" height="16" rx="2" fill="#F18877"/><path d="M2 2l10 8 10-8" stroke="#fff" stroke-width="2" fill="none"/></svg></span>info@drhelgabrunsvik.com</div>
  <nav class="abs main-nav">
    <a class="current" href="#">Home</a><a href="#">About</a><a href="#">Services</a><a href="#">Contact</a><a href="#">Free Resources</a>
  </nav>
</header>

<section class="hero">
  <div class="hero-media" role="img" aria-label="Background video of a joyful woman with arms outstretched in a green meadow"></div>
  <h1 class="abs hero-title">LIVE YOUR BEST LIFE:<br>HAPPY &amp; HEALTHY &amp; FULL OF JOY!</h1>
  <div class="abs watch"><svg width="34" height="34" viewBox="0 0 34 34"><circle cx="17" cy="17" r="17" fill="#fff"/><path d="M13 10l11 7-11 7z" fill="#2d3428"/></svg>WATCH VIDEO</div>
  <svg class="abs chevron" width="32" height="18" viewBox="0 0 32 18"><path d="M3 3l13 12L29 3" stroke="#fff" stroke-width="3" fill="none"/></svg>
</section>

<section class="talk-bar">
  <div class="abs talk-title">Free Health Talk</div>
  <div class="abs join"><svg width="36" height="28" viewBox="0 0 24 18"><rect x="1" y="1" width="22" height="16" rx="2" fill="#F18877"/><path d="M2 2l10 8 10-8" stroke="#fff" stroke-width="2" fill="none"/></svg>JOIN MY LIST TODAY</div>
  <svg class="abs" style="left:895px;top:40px" width="48" height="84" viewBox="0 0 48 84"><line x1="44" y1="2" x2="4" y2="82" stroke="#bbb" stroke-width="2"/></svg>
  <div class="abs social-row"><span></span><span></span><span></span></div>
</section>

<section class="about">
  <div class="abs about-band"></div>
  <div class="abs about-ring"></div>
  <div class="abs about-inner"></div>
  <div class="abs about-photo" role="img" aria-label="Portrait of the doctor kneeling in the grass with her two dogs"></div>
  <h2 class="abs about-title">About Dr Helga Brunsvik</h2>
  <p class="abs about-lead">Unlock the Power of Joy and Well-Being: Discover Simple Steps to Restore Your Happiness and Health Today!</p>
  <p class="abs about-text">With over 30 years of being a doctor, I've met countless people facing ongoing health issues and struggles that couldn't be solved solely through conventional medicine. That's why it's so important to embrace a holistic approach in our quest for balance.</p>
  <div class="abs btn-coral about-btn">MORE ABOUT ME</div>
</section>

<section class="services">
  <h2 class="abs section-title">Our Services</h2>

  <article class="abs service s1">
    <div class="service-photo photo-left" role="img" aria-label="Woman laughing with arms wide open in a flowering meadow" style="background:linear-gradient(135deg,#2f4a26,#6f8a4e 55%,#c8cdb0)"></div>
    <div class="service-body body-right">
      <h3>Stress management consultant</h3>
      <p>Lorem ipsum dolor sit amet, consectetur adipiscing elit, sed do eiusmod tempor incididunt Lorem ipsum dolor sit amet, consectetur adipiscing elit, sed do eiusmod tempor incididunt Lorem ipsum dolor sit amet, consecte tur adipiscing elit, sed do eiusmod tempor incididunt</p>
      <div class="read-more">READ MORE <svg width="20" height="10" viewBox="0 0 20 10"><path d="M0 5h17M13 1l4 4-4 4" stroke="#F18877" stroke-width="2" fill="none"/></svg></div>
    </div>
  </article>

  <article class="abs service s2">
    <div class="service-body body-left">
      <h3>General Practitioner</h3>
      <p>Lorem ipsum dolor sit amet, consectetur adipiscing elit, sed do eiusmod tempor incididunt Lorem ipsum dolor sit amet, consectetur adipiscing elit, sed do eiusmod tempor incididunt Lorem ipsum dolor sit amet, consecte tur adipiscing elit, sed do eiusmod tempor incididunt</p>
      <div class="read-more"><svg width="20" height="10" viewBox="0 0 20 10"><path d="M20 5H3M7 1L3 5l4 4" stroke="#F18877" stroke-width="2" fill="none"/></svg> READ MORE</div>
    </div>
    <div class="service-photo photo-right" role="img" aria-label="Doctor smiling while kneeling with her two dogs on a lawn" style="background:linear-gradient(135deg,#5d7a3e,#8aa062 50%,#b6a68e)"></div>
  </article>

  <article class="abs service s3">
    <div class="service-photo photo-left" role="img" aria-label="Close-up portrait of the coach smiling outdoors" style="background:linear-gradient(135deg,#6d7f48,#b89c7e 55%,#d8b9a0)"></div>
    <div class="service-body body-right">
      <h3>Health and Well-Being coach</h3>
      <p>Lorem ipsum dolor sit amet, consectetur adipiscing elit, sed do eiusmod tempor incididunt Lorem ipsum dolor sit amet, consectetur adipiscing elit, sed do eiusmod tempor incididunt Lorem ipsum dolor sit amet, consecte tur adipiscing elit, sed do eiusmod tempor incididunt</p>
      <div class="read-more">READ MORE <svg width="20" height="10" viewBox="0 0 20 10"><path d="M0 5h17M13 1l4 4-4 4" stroke="#F18877" stroke-width="2" fill="none"/></svg></div>
    </div>
  </article>
</section>

<section class="cta">
  <p class="abs cta-title">Lorem ipsum dolor sit amet,<br>consectetur adipiscing elit</p>
  <div class="abs cta-btn cta-site">brightpathdaily</div>
  <div class="abs cta-btn cta-contact">Contact Us</div>
</section>

<section class="testimonials">
  <h2 class="abs section-title">Testimonials</h2>

  <article class="abs quote-card t1">
    <div class="quote-mark">“</div>
    <div class="stars"><svg width="110" height="18" viewBox="0 0 110 18"><g fill="#F18877"><path id="st" d="M9 0l2.6 6 6.4.5-4.9 4.2 1.5 6.3L9 13.6 3.4 17l1.5-6.3L0 6.5 6.4 6z"/><use href="#st" x="22"/><use href="#st" x="44"/><use href="#st" x="66"/><use href="#st" x="88"/></g></svg></div>
    <p>Lorem ipsum dolor sit amet, con secte tur adipiscing elit. Pellen tesque aliquet eros vitae placerat</p>
    <div class="author"><span class="avatar" role="img" aria-label="Client photo"></span><div><b>Lorem ipsum sit</b><span>Lorem ipsum</span></div></div>
  </article>

  <article class="abs quote-card t2">
    <div class="quote-mark">“</div>
    <div class="stars"><svg width="110" height="18" viewBox="0 0 110 18"><g fill="#F18877"><use href="#st"/><use href="#st" x="22"/><use href="#st" x="44"/><use href="#st" x="66"/><use href="#st" x="88"/></g></svg></div>
    <p>Lorem ipsum dolor sit amet, con secte tur adipiscing elit. Pellen tesque aliquet eros vitae placerat</p>
    <div class="author"><span class="avatar" role="img" aria-label="Client photo"></span><div><b>Lorem ipsum sit</b><span>Lorem ipsum</span></div></div>
  </article>

  <article class="abs quote-card t3">
    <div class="quote-mark">“</div>
    <div class="stars"><svg width="110" height="18" viewBox="0 0 110 18"><g fill="#F18877"><use href="#st"/><use href="#st" x="22"/><use href="#st" x="44"/><use href="#st" x="66"/><use href="#st" x="88"/></g></svg></div>
    <p>Lorem ipsum dolor sit amet, con secte tur adipiscing elit. Pellen tesque aliquet eros vitae placerat</p>
    <div class="author"><span class="avatar" role="img" aria-label="Client photo"></span><div><b>Lorem ipsum sit</b><span>Lorem ipsum</span></div></div>
  </article>

  <div class="abs dots"><span></span><span></span><span></span><span></span></div>
</section>

<section class="newsletter">
  <h2 class="abs newsletter-title">Get Regular Inspiration for Health,<br>Wellbeing and Happiness</h2>
  <p class="abs newsletter-sub">Sing up to my awesome Newsletter Mailinglist</p>
  <div class="abs newsletter-form"><span class="field">Enter Email Address</span><span class="subscribe">SUBSCRIBE</span></div>
</section>

<footer class="site-footer">
  <div class="abs footer-brand"><i></i>Dr Helga Brunsvik</div>

  <h4 class="abs footer-heading fh1">Contact Us</h4>
  <h4 class="abs footer-heading fh2">Address</h4>
  <h4 class="abs footer-heading fh3">Quick Links</h4>

  <div class="abs input f-first">First Name :</div>
  <div class="abs input f-last">Last Name :</div>
  <div class="abs input f-email">Email :</div>
  <div class="abs input f-phone">Phone :</div>
  <div class="abs input f-message">Message :</div>
  <div class="abs f-submit">SUBMIT</div>

  <div class="abs contact-item ci1">
    <span class="contact-icon"><svg width="18" height="24" viewBox="0 0 18 24"><path d="M9 0a9 9 0 019 9c0 6-9 15-9 15S0 15 0 9a9 9 0 019-9z" fill="#fff"/><circle cx="9" cy="9" r="3.5" fill="#F18877"/></svg></span>
    <div><b>ADDRESS</b><span>Address line here dummy<br>address line here</span></div>
  </div>
  <div class="abs contact-item ci2">
    <span class="contact-icon"><svg width="20" height="20" viewBox="0 0 24 24"><path d="M6.6 10.8a15 15 0 006.6 6.6l2.2-2.2c.3-.3.7-.4 1-.2 1.1.4 2.3.6 3.6.6.6 0 1 .4 1 1V20c0 .6-.4 1-1 1A17 17 0 013 4c0-.6.4-1 1-1h3.5c.6 0 1 .4 1 1 0 1.2.2 2.4.6 3.6.1.3 0 .7-.2 1z" fill="#fff"/></svg></span>
    <div><b>PHONE NUMBER</b><span>(+0123) 1234567890</span></div>
  </div>
  <div class="abs contact-item ci3">
    <span class="contact-icon"><svg width="20" height="16" viewBox="0 0 24 18"><rect x="1" y="1" width="22" height="16" rx="2" fill="#fff"/><path d="M2 2l10 8 10-8" stroke="#F18877" stroke-width="2" fill="none"/></svg></span>
    <div><b>EMAIL US</b><span>info@drhelgabrunsvik.com</span></div>
  </div>

  <ul class="abs quick-links"><li>About</li><li>Services</li><li>Contact</li><li>Free Resources</li></ul>
  <div class="abs footer-social"><span></span><span></span><span></span><span></span></div>

  <div class="abs footer-rule"></div>
  <p class="abs copyright">Copyright © 2023 All Rights Reserved By Dr. Helga Brunsvik</p>
  <p class="abs legal">Disclaimer &nbsp;|&nbsp; Privacy</p>
</footer>

</body>
</html>
```